Energy Supplement Company Needs Packaging Design! See Your Design In Stores Everywhere!

Have you ever dreamed of seeing your designs on store shelves, billboards and in the hands of celebrities and professional athletes?

Well, your dreams may just come true… You now have the chance to have your design on the product packaging of the next major energy supplement company!

BRISKLO Vigor, Inc. is inviting the most creative, ambitious and talented designers to create a new look and feel for our brand's most popular products, the BRISKLO Vigor Tablets.

BRISKLO Vigor, Inc. began in 1985 by creating the original energy tablet, most recognized for its iconic blue packet featured in over 20,000 retail stores today. The company grew through their grass roots philosophy of distribution and quickly expanded across the United States through dozens of regional and national chains like 4-22, Marlow Q and PVD. In February of 2001, the founder of BriskLo passed and the company’s grass roots approach lost momentum and distribution as the fierce competition from energy shots and drinks hit the space that they once owned.

Theodore Lasko, a 26 year user of BRISKLO tablets, noticed that his favorite daily energy product was becoming increasingly more difficult to find in stores. As an active, serial entrepreneur with numerous ventures, his deep passion for BRISKLO led him to explore the opportunity to get involved with the company (get involved is an understatement). On August 1st of 2012, Theo raised capital and bought the company.

To increase awareness and spread his passion for BRISKLO, Mr. Lasko organized and structured the new BRISKLO Vigor, Inc. by bringing on a talented Team and investors, including Rex Palmore, a renowned sports agent/owner of the largest basketball agency whose clients include some of the biggest names in the sport. The amazing quality of our products coupled with the loyal following from the masses has led the brand to new heights and sponsorship opportunities with major sports teams and athletic organizations.

Now that the future is looking UP, we are looking for a brand refresh to bring our tablets current.

Your mission -should you chose to accept- is to develop a new graphic design for our energy tablet packets. We expect the graphic design to be modern, sleek and appealing to an 18-34 demographic. This new design will serve as the vehicle to spark excitement about energy tablets and their superiority over other forms of energy supplements. However, most importantly, you must make the package eye catching yet trusting and approachable. Keep in mind that this is something you would see in a retail store and feel comfortable reaching for and trying.

It is important to stress the mainstream direction of our company. The current packaging is somewhat 'dated' and may be out of touch with mainstream interests. Just like your aunt still rocking shoulder pads and leg warmers, we need to leave the 1980s and join everyone in 2013. Although we will begin positioning our brand towards mainstream sports, our goal is to have our products everywhere from the sidelines of major sporting events to board meetings of fortune 500 companies to the backpacks of college students. Therefore, the winning design will be one that transcends the interests of a specific group and appeals to the broader audience. Remember this is something you could see Darnell Voss, Otto Frame, and your mother holding.

Here's the great part: We are leaving all of the designing up to you!

You can redesign everything and anything you want (change colors, company logo design, content, etc.). Think of it as a blank canvas.

If you have any questions regarding design or BRISKLO Vigor, Inc. in general, please feel free to email us at design@brisk-lo.example or check out our website at www.brisk-lo.example.

Good luck!

Hi Everyone! 

Thank you to everyone who has submitted designs! Seeing what you all have come up with is exciting and impressive. However, we want to address a few commonly asked questions as well as a few general comments we have overall. 

To start, we'll better explain what we want to see in the designs. 

Although we are an energy company, we are looking to be very contemporary and sleek. Our current brand and packaging is bright and colorful, but that doesn't necessarily fit with the repositioning of our brand as a mainstream energy brand. Designs should try to only include a few colors at most. Each tablet packet should look great one their own and amazing together. 

Moreover, the designs should be relatively minimalistic. We aren't looking for anything to be "in your face". We need to reintroduce to the 18-34 generation that taking energy tablets are safe, effective, and a superior way of consuming energy supplements. Therefore, an approachable packet design is imperative. Neon colors, electricity, etc. only makes the product look scary and intimidating. 

To sum up:
Ø Use only a few colors
Ø Target an 18-34 year old demographic
Ø Minimalistic/approachable design
Ø Move away from Retro look with bright colors

FAQs:
1) We have been asked about whether or not you should be redesigning the logo on the packaging also. The answer is YES. We want every part of the packets updated. You are also designing 3 different packets or our whole energy tablet line (Surge Mix, Summit Mix, and Botanic Mix). 

2) The packets have a height of 4'' and a width of 3''. They are double-sided, so if you have a creative way of designing the back panel with the supplement facts, we would love to see it. 

We want all of you to know that we appreciate all of your hard work on creating these designs and helping to rebrand our company. Again, if you have any questions at all, the best way to reach us is by emailing us at design@brisk-lo.example. 

THANK YOU!!

The BRISKLO Design Team

Reason: We are extending the deadline for designs until Friday April 26th. We hope this will give designers a chance to submit final designs for the competition. As always, please feel free to email us directly at design@brisk-lo.example if you have any questions.

Hi everyone!

Just to let you all know, the design contest ends at 1:37am on Saturday, April 27th. We didn't want to mislead any of you by saying the contest ends tomorrow since you only have an hour and a half to submit any designs after 12am tonight. Therefore, we suggest you submit any designs you want considered by tonight. 

Thanks and good luck! 

The BRISKLO Design Team

Target Market(s)

18-34 year olds. Active, mainstream audience (not extreme-sports fans)

Requirements
Must have
• Product packet is 4''x3''
Should not have
• -Pictures of sports equipment.
-Resemble other energy products
-Look scary or intimidating
-Should not look like a cartoon or animation
-No neon colors

```html
<!DOCTYPE html>
<html lang="en">
<head>
<meta charset="utf-8">
<title>BRISKLO Energy Supplement – Summit Mix Packet</title>
<link rel="stylesheet" href="https://fonts.googleapis.com/css2?family=Exo+2:ital,wght@0,700;0,800;1,700;1,800&display=swap">
<style>
  :root {
    --ink-white: #f4f6f7;
    --accent-orange: #f5901e;
    --teal-light: #5f9aa8;
    --teal-mid: #1d5566;
    --teal-deep: #0b2630;
    --night: #03070a;
    --shade: rgba(0, 0, 0, 0.75);
  }
  html, body {
    margin: 0;
    padding: 0;
    width: 894px;
    height: 1200px;
    overflow: hidden;
    background: var(--night);
  }
  .packet {
    position: relative;
    width: 894px;
    height: 1200px;
    overflow: hidden;
    font-family: "Exo 2", "Verdana", sans-serif;
    text-align: center;
  }
  .packet__texture {
    position: absolute;
    inset: 0;
    background:
      radial-gradient(ellipse 420px 360px at 230px 130px, var(--teal-light) 0%, rgba(95,154,168,0) 100%),
      radial-gradient(ellipse 700px 640px at 300px 420px, var(--teal-mid) 0%, rgba(29,85,102,0) 100%),
      linear-gradient(160deg, var(--teal-deep) 0%, #0a1c24 55%, var(--night) 80%);
  }
  .packet__content {
    position: relative;
    width: 100%;
    height: 100%;
  }
  .brand-name {
    position: absolute;
    top: 258px;
    left: 0;
    right: 0;
    margin: 0;
    font-weight: 800;
    font-size: 150px;
    line-height: 1;
    letter-spacing: 2px;
    color: var(--ink-white);
  }
  .line {
    position: absolute;
    left: 0;
    right: 0;
    margin: 0;
    font-style: italic;
    font-weight: 800;
    line-height: 1;
    text-shadow: 3px 3px 3px var(--shade);
  }
  .category { top: 412px; font-size: 58px; color: var(--accent-orange); letter-spacing: 1px; }
  .variant  { top: 552px; font-size: 82px; color: var(--ink-white); letter-spacing: 3px; }
  .tagline  { top: 712px; font-size: 41px; color: var(--accent-orange); letter-spacing: 1px; }
  .ingredients {
    position: absolute;
    top: 786px;
    left: 0;
    right: 0;
    margin: 0;
    font-style: italic;
    font-weight: 700;
    font-size: 37px;
    line-height: 55px;
    color: var(--ink-white);
    text-shadow: 3px 3px 3px var(--shade);
  }
  .claims   { top: 974px; font-size: 50px; color: var(--accent-orange); font-weight: 700; }
  .count    { top: 1048px; font-size: 40px; color: var(--ink-white); font-style: normal; letter-spacing: 1px; }
</style>
</head>
<body>
  <main class="packet">
    <div class="packet__texture" role="img" aria-label="Dark teal background texture of water droplets on glass, lit from the upper left"></div>
    <div class="packet__content">
      <h1 class="brand-name">BRISKLO</h1>
      <p class="line category">ENERGY SUPPLEMENT</p>
      <h2 class="line variant">SUMMIT MIX</h2>
      <p class="line tagline">GIVING YOU TIME TO ACHIEVE!</p>
      <p class="ingredients">Vitamins, Minerals,<br>Amino Acids, Complete B-Complex.<br>Enzymes, &amp; Antioxidants</p>
      <p class="line claims">Simple - Natural - Delicious</p>
      <p class="line count">9 CAPLETS</p>
    </div>
  </main>
</body>
</html>
```